Business Card Project for Firm Deck Hoisting

Business name is "Firm Deck Hoisting" we are a scaffolding & rigging business specialising in local and remote work for:
- scaffolding (residential, commercial, industrial)
- rigging
-man material hoists
- swing stages
- labour hire

On the back of the card I would like FDH as the symbol / logo. I have attached the logos we have had created by sketch harbour. We would like to use bold colours – preferably as the same colour scheme as the logo.

Target Market(s)

Construction business

Industry/Entity Type

Construction

Contact Information for Business Card

name: Owen Pellew
Title: Director
Phone: 0491 572 864
Address: PO BOX 3251, Harwick SA 5170
Email: owen@firmdeckhoisting.com.au
Website: www.firmdeckhoisting.com.au

Font styles to use
Sans Serif

Requirements
Must have
• Must use existing logo & prefering using bold colours
Nice to have
• Would be nice to have a line of dot points in what we specialise in but not essential
• Would be nice to see some designs with a slogan but not essential
Should not have
• NA

```html
<!DOCTYPE html>
<html lang="en">
<head>
<meta charset="utf-8">
<title>Firm Deck Hoisting – Business Card</title>
<link rel="stylesheet" href="https://fonts.googleapis.com/css2?family=Source+Sans+3:wght@400;600;700&display=swap">
<style>
  :root {
    --brand-blue: #0f75bc;
    --brand-black: #231f20;
    --card-white: #ffffff;
    --backdrop: #4b4b4b;
    --text-on-dark: #ffffff;
  }
  * { margin: 0; padding: 0; box-sizing: border-box; }
  html, body {
    width: 1200px; height: 1200px; overflow: hidden;
    background: var(--backdrop);
    font-family: "Source Sans 3", sans-serif;
  }
  .card {
    position: absolute; left: 214px; width: 772px; height: 437px;
    border-radius: 16px; overflow: hidden;
  }
  /* Front */
  .card-front { top: 126px; background: var(--brand-black); color: var(--text-on-dark); }
  .card-front .wordmark {
    position: absolute; top: 132px; left: 0; width: 100%;
    text-align: center; font-size: 40px; line-height: 48px; font-weight: 700; letter-spacing: 1px;
    color: var(--text-on-dark);
  }
  .service-band {
    position: absolute; top: 212px; left: 0; width: 100%; height: 144px;
    background: var(--brand-blue);
    display: flex; flex-direction: column; justify-content: center; align-items: center;
    font-size: 25px; line-height: 30px;
  }
  .service-band .sep { margin: 0 4px; opacity: .85; }
  .card-front .website {
    position: absolute; top: 385px; width: 100%; text-align: center; font-size: 24px; line-height: 30px;
  }
  /* Back */
  .card-back { top: 638px; background: var(--card-white); }
  .card-back .swoosh { position: absolute; inset: 0; }
  .card-back .wordmark {
    position: absolute; top: 62px; left: 326px; width: 416px;
    text-align: center; font-size: 36px; line-height: 44px; font-weight: 700; letter-spacing: 1px;
    color: var(--brand-black);
  }
  .person { position: absolute; top: 212px; left: 442px; width: 280px; text-align: center; }
  .person .name { font-size: 34px; font-weight: 700; color: var(--brand-blue); line-height: 40px; }
  .person .title { font-size: 24px; color: var(--brand-black); line-height: 30px; }
  .contact { position: absolute; left: 28px; top: 277px; color: var(--text-on-dark); font-size: 23px; }
  .contact-row { display: flex; align-items: center; height: 30px; }
  .contact-row svg { width: 26px; height: 22px; margin-right: 9px; flex: none; }
  .address { position: absolute; left: 28px; top: 380px; color: var(--text-on-dark); font-size: 24px; line-height: 30px; }
</style>
</head>
<body>

<section class="card card-front">
  <div class="wordmark">Firm Deck Hoisting</div>
  <div class="service-band">
    <div>scaffolding (residential, commercial, industrial)</div>
    <div>rigging<span class="sep">|</span>man material hoists<span class="sep">|</span>swing stages<span class="sep">|</span>labour hire</div>
  </div>
  <div class="website">www.firmdeckhoisting.com.au</div>
</section>

<section class="card card-back">
  <svg class="swoosh" viewBox="0 0 772 437" preserveAspectRatio="none" aria-hidden="true">
    <rect width="772" height="437" fill="var(--brand-blue)"/>
    <path d="M228 0 C250 230 470 400 700 437 L740 437 C500 385 300 210 278 0 Z" fill="var(--brand-black)"/>
    <path d="M278 0 C300 210 500 385 740 437 L772 437 L772 0 Z" fill="var(--card-white)"/>
  </svg>
  <div class="wordmark">Firm Deck Hoisting</div>
  <div class="person">
    <div class="name">Owen Pellew</div>
    <div class="title">Director</div>
  </div>
  <div class="contact">
    <div class="contact-row">
      <svg viewBox="0 0 26 22" aria-hidden="true"><path d="M2 8 C2 2 24 2 24 8 L24 10 L18 10 L18 7 L8 7 L8 10 L2 10 Z M6 11 L20 11 L23 20 L3 20 Z" fill="#fff"/><circle cx="13" cy="15" r="3" fill="var(--brand-blue)"/></svg>
      <span>0491 572 864</span>
    </div>
    <div class="contact-row">
      <svg viewBox="0 0 26 22" aria-hidden="true"><rect x="2" y="4" width="22" height="15" fill="none" stroke="#fff" stroke-width="2"/><path d="M2 4 L13 13 L24 4 M2 19 L10 11 M24 19 L16 11" fill="none" stroke="#fff" stroke-width="2"/></svg>
      <span>owen@firmdeckhoisting.com.au</span>
    </div>
    <div class="contact-row">
      <svg viewBox="0 0 26 22" aria-hidden="true"><g fill="none" stroke="#fff" stroke-width="1.6"><circle cx="13" cy="11" r="9.5"/><ellipse cx="13" cy="11" rx="4.5" ry="9.5"/><path d="M3.5 11 H22.5 M5 6 H21 M5 16 H21"/></g></svg>
      <span>www.firmdeckhoisting.com.au</span>
    </div>
  </div>
  <div class="address">PO BOX 3251, Harwick SA 5170</div>
</section>

</body>
</html>
```